Clean professional business card design

Need a professional looking, high quality card and letterhead design. Business card would prefer to have a grey tone to the background.

Back of card needs to have: "Securities offered through Norvane Capital Partners LLC (doing Insurance business in CA as NKPTR Insurance Agency), member BRAXEL/TOVMA. Advisory services offered through Norvane Wealth Counsel LLC. Norvane entities are under separate ownership from any other named entity. [employee name] CA Insurance Lic #7K21904

Industry/Entity Type

Financial Planning

Font styles to use
Serif
Sans Serif

Requirements
Must have
• Customization of text so that I can adjust for other employee

```html
<!DOCTYPE html>
<html lang="en">
<head>
<meta charset="utf-8">
<title>Keystead Financial Advisers – Stationery</title>
<link href="https://fonts.googleapis.com/css2?family=Cormorant+Garamond:wght@500&family=Open+Sans:wght@400;600&family=Raleway:wght@300&display=swap" rel="stylesheet">
<style>
  :root{
    --brand-blue:#1275bf;
    --band-grey:#77787b;
    --ink:#2a2a2a;
    --muted:#9a9ca0;
    --paper:#ffffff;
    --backdrop:#ebebeb;
  }
  *{box-sizing:border-box;margin:0;padding:0}
  html,body{width:1200px;height:1000px;overflow:hidden;background:var(--backdrop)}
  body{position:relative;font-family:"Open Sans",sans-serif;color:var(--ink)}
  .sheet{position:absolute;background:var(--paper);overflow:hidden}
  .footer-band{position:absolute;left:0;bottom:0;width:100%;display:block}
  .footer-url{position:absolute;color:#fff;font-weight:600}

  /* brand lockup */
  .lockup{position:absolute;text-align:center}
  .lockup-square{display:block;margin:0 auto;background:var(--brand-blue)}
  .lockup-name{font-family:"Cormorant Garamond",serif;font-weight:500;color:var(--brand-blue);text-transform:uppercase;line-height:1;letter-spacing:.02em}
  .lockup-tag{font-family:"Raleway",sans-serif;font-weight:300;color:var(--muted);text-transform:uppercase;letter-spacing:.18em;line-height:1}

  /* letterhead */
  .letterhead{left:101px;top:185px;width:469px;height:610px}
  .letterhead .lockup{left:30px;top:38px;width:134px}
  .letterhead .lockup-square{width:22px;height:22px;margin-bottom:10px}
  .letterhead .lockup-name{font-size:19px}
  .letterhead .lockup-tag{font-size:8px;margin-top:3px;letter-spacing:.16em}
  .contact{position:absolute;left:342px;top:47px;padding-left:10px;border-left:1px solid #b5b5b5;font-size:7px;line-height:9.5px}
  .contact .gap{height:6px}
  .contact-row{display:flex;align-items:center;gap:4px}
  .contact-row svg{width:6px;height:6px;fill:var(--brand-blue)}
  .letterhead .footer-url{right:32px;bottom:8px;font-size:8px}

  /* business card front */
  .card-front{left:641px;top:185px;width:219px;height:123px}
  .card-front .lockup{left:12px;top:14px;width:70px}
  .card-front .lockup-square{width:10px;height:10px;margin-bottom:6px}
  .card-front .lockup-name{font-size:9.5px}
  .card-front .lockup-tag{font-size:4px;margin-top:1px;letter-spacing:.14em}
  .holder{position:absolute;right:13px;top:69px;text-align:right;width:120px}
  .holder-name{font-size:7.5px;font-weight:600;color:var(--brand-blue);line-height:1}
  .holder-role{font-size:4.5px;margin-top:1px;padding-bottom:2px;border-bottom:1px solid #b5b5b5}
  .card-rule{position:absolute;left:12px;top:85px;width:110px;border-top:1px solid #b5b5b5}
  .card-contact{position:absolute;left:12px;top:89px;font-size:4.6px;line-height:6.5px}
  .card-contact .contact-row svg{width:4px;height:4px}
  .card-address{position:absolute;right:13px;top:95px;text-align:right;font-size:4.6px;line-height:6.5px}
  .card-front .footer-url{right:13px;bottom:2px;font-size:4.6px}

  /* business card back */
  .card-back{left:874px;top:185px;width:213px;height:123px;background:var(--brand-blue)}
  .card-back .lockup{left:0;top:36px;width:100%}
  .card-back .lockup-square{width:16px;height:16px;margin-bottom:9px;background:#fff}
  .card-back .lockup-name{font-size:14px;color:#fff}
  .card-back .lockup-tag{font-size:7px;color:#fff;margin-top:2px;letter-spacing:.16em}

  /* envelope front */
  .envelope-front{left:640px;top:362px;width:446px;height:202px}
  .envelope-front .lockup{left:16px;top:20px;width:90px}
  .envelope-front .lockup-square{width:14px;height:14px;margin-bottom:8px}
  .envelope-front .lockup-name{font-size:12px}
  .envelope-front .lockup-tag{font-size:5.5px;margin-top:1px}
  .return-address{position:absolute;left:16px;top:160px;font-size:5.5px;line-height:7px}
  .envelope-front .footer-url{right:29px;bottom:6px;font-size:7px}

  /* envelope back */
  .envelope-back{left:639px;top:590px;width:452px;height:208px}
  .envelope-flap{position:absolute;left:0;top:0;width:100%;height:67px;display:block}
</style>
</head>
<body>

<section class="sheet letterhead" aria-label="Letterhead">
  <div class="lockup">
    <span class="lockup-square"></span>
    <div class="lockup-name">Keystead</div>
    <div class="lockup-tag">Financial Advisers</div>
  </div>
  <div class="contact">
    <div>55 demo street, demo place</div>
    <div>P.O. Box 000, 555 Avenue</div>
    <div class="gap"></div>
    <div class="contact-row"><svg viewBox="0 0 10 10"><path d="M2 0l2 2-1 2 3 3 2-1 2 2-2 2C4 10 0 6 0 2z"/></svg>000-0000-0000</div>
    <div class="contact-row"><svg viewBox="0 0 10 10"><path d="M2 0l2 2-1 2 3 3 2-1 2 2-2 2C4 10 0 6 0 2z"/></svg>000-0000-0000</div>
    <div class="contact-row"><svg viewBox="0 0 10 10"><path d="M0 2h10v6H0z M0 2l5 3 5-3" /></svg>hello@keysteadfa.com</div>
  </div>
  <svg class="footer-band" viewBox="0 0 469 24" height="24" preserveAspectRatio="none">
    <rect x="0" y="4" width="290" height="5" fill="var(--band-grey)"/>
    <path d="M0 14H280C300 14 300 0 330 0H469V24H0Z" fill="var(--brand-blue)"/>
    <path d="M0 12H282C300 12 302 -1 330 -1" fill="none" stroke="#fff" stroke-width="2"/>
  </svg>
  <span class="footer-url">www.keysteadfa.com</span>
</section>

<section class="sheet card-front" aria-label="Business card front">
  <div class="lockup">
    <span class="lockup-square"></span>
    <div class="lockup-name">Keystead</div>
    <div class="lockup-tag">Financial Advisers</div>
  </div>
  <div class="holder">
    <div class="holder-name">Adrian Vell</div>
    <div class="holder-role">General Manager</div>
  </div>
  <div class="card-rule"></div>
  <div class="card-contact">
    <div class="contact-row"><svg viewBox="0 0 10 10"><path d="M2 0l2 2-1 2 3 3 2-1 2 2-2 2C4 10 0 6 0 2z"/></svg>000-0000-0000</div>
    <div class="contact-row"><svg viewBox="0 0 10 10"><path d="M2 3h6v4H2z M3 0h4v3H3z"/></svg>000-0000-0000</div>
    <div class="contact-row"><svg viewBox="0 0 10 10"><path d="M0 2h10v6H0z"/></svg>hello@keysteadfa.com</div>
  </div>
  <div class="card-address">
    <div>55 demo street, demo place</div>
    <div>P.O. Box 000, 555 Avenue</div>
  </div>
  <svg class="footer-band" viewBox="0 0 219 11" height="11" preserveAspectRatio="none">
    <rect x="0" y="1" width="135" height="3" fill="var(--band-grey)"/>
    <path d="M0 7H130C140 7 140 0 155 0H219V11H0Z" fill="var(--brand-blue)"/>
    <path d="M0 5.8H131C140 5.8 141 -0.6 155 -0.6" fill="none" stroke="#fff" stroke-width="1"/>
  </svg>
  <span class="footer-url">www.keysteadfa.com</span>
</section>

<section class="sheet card-back" aria-label="Business card back">
  <div class="lockup">
    <span class="lockup-square"></span>
    <div class="lockup-name">Keystead</div>
    <div class="lockup-tag">Financial Advisers</div>
  </div>
</section>

<section class="sheet envelope-front" aria-label="Envelope front">
  <div class="lockup">
    <span class="lockup-square"></span>
    <div class="lockup-name">Keystead</div>
    <div class="lockup-tag">Financial Advisers</div>
  </div>
  <div class="return-address">
    <div>55 demo street, demo place</div>
    <div>P.O. Box 000, 555 Avenue</div>
  </div>
  <svg class="footer-band" viewBox="0 0 446 20" height="20" preserveAspectRatio="none">
    <rect x="0" y="3" width="272" height="5" fill="var(--band-grey)"/>
    <path d="M0 12H265C285 12 285 0 315 0H446V20H0Z" fill="var(--brand-blue)"/>
    <path d="M0 10H267C285 10 287 -1 315 -1" fill="none" stroke="#fff" stroke-width="2"/>
  </svg>
  <span class="footer-url">www.keysteadfa.com</span>
</section>

<section class="sheet envelope-back" aria-label="Envelope back">
  <svg class="envelope-flap" viewBox="0 0 452 67" preserveAspectRatio="none">
    <path d="M0 0H452C446 20 446 55 432 63C430 66 428 66 420 66H30C22 66 20 66 16 62C8 50 8 20 0 0Z" fill="var(--brand-blue)"/>
    <circle cx="226" cy="33" r="7" fill="#fff"/>
  </svg>
</section>

</body>
</html>
```